Design a website for a quickly growing ghostwriting and editing firm

NRB Productions has a website through Wix, but we need help! We are based in Austin, TX, and we work primarily with self-help, wellness, and diet authors. We offer ghostwriting, editing and book development services. You can see our basic site now at www.nadiabrentproductions.example

```html
<!DOCTYPE html>
<html lang="en">
<head>
<meta charset="utf-8">
<title>NRB Productions — Ghostwriting &amp; Editing</title>
<link rel="stylesheet" href="https://fonts.googleapis.com/css2?family=Montserrat:wght@400;500;600;700;800&family=Nunito+Sans:wght@400;600;700&display=swap">
<style>
:root{
  --orange:#c77b2b;
  --orange-dark:#a85f18;
  --orange-light:#e3a459;
  --ink:#27283a;
  --muted:#6b6b76;
  --blush:#f8efeb;
  --paper:#ffffff;
  --footer:#efefef;
  --line:#d9d3cf;
}
*{margin:0;padding:0;box-sizing:border-box}
html,body{width:1200px;height:4112px;overflow:hidden}
body{font-family:"Nunito Sans",Arial,sans-serif;color:var(--ink);background:var(--paper);position:relative}
h1,h2,h3,h4,.btn,.nav a,.brand{font-family:"Montserrat",Arial,sans-serif}
section,header,footer{position:absolute;left:0;width:1200px}
.abs{position:absolute}

/* header */
.site-header{top:0;height:80px;background:var(--paper);box-shadow:0 2px 8px rgba(0,0,0,.06);z-index:3}
.brand{position:absolute;left:80px;top:22px;display:flex;align-items:center;gap:12px;font-weight:700;font-size:24px;color:var(--orange-dark);letter-spacing:.5px}
.brand .mark{width:30px;height:30px;border-radius:50%;background:var(--orange)}
.nav{position:absolute;left:380px;top:0;height:80px;display:flex;align-items:center;gap:36px}
.nav a{font-size:12px;font-weight:600;color:var(--ink);text-decoration:none;letter-spacing:.6px;position:relative;padding:8px 0}
.nav a.active{color:var(--orange)}
.nav a.active::after{content:"";position:absolute;left:0;right:0;bottom:0;height:2px;background:var(--orange)}
.nav .search{margin-left:8px}

/* hero */
.hero{top:80px;height:640px;background:linear-gradient(120deg,#2f2a26 0%,#574535 40%,#8b6c48 75%,#c79a5f 100%)}
.hero .photo{position:absolute;inset:0}
.hero .shade{position:absolute;inset:0;background:rgba(20,16,12,.45)}
.hero .kicker{position:absolute;top:200px;width:100%;text-align:center;color:#fff;font-family:"Montserrat",sans-serif;font-size:16px;letter-spacing:6px;font-weight:500}
.hero h1{position:absolute;top:232px;width:100%;text-align:center;color:#fff;font-size:50px;line-height:56px;font-weight:800;letter-spacing:1px}
.btn{display:inline-block;font-size:12px;font-weight:700;letter-spacing:.8px;border-radius:22px;text-decoration:none}
.btn-solid{background:var(--orange);color:#fff;padding:12px 28px}
.btn-outline{border:2px solid var(--orange);color:var(--orange);padding:11px 26px;background:transparent}
.hero .btn{position:absolute;top:352px;left:530px}
.hero .arrow{position:absolute;top:300px}

/* about */
.about{top:720px;height:600px}
.about .blob{position:absolute;left:0;top:40px}
.eyebrow{font-family:"Montserrat",sans-serif;font-size:15px;font-weight:600;letter-spacing:2px;color:var(--orange)}
.section-title{font-size:32px;font-weight:700;color:var(--ink);letter-spacing:.5px}
.rule{width:70px;height:3px;background:var(--orange)}
.about .copy{position:absolute;left:608px;top:172px;width:500px}
.about .section-title{margin-top:6px}
.about .rule{margin-top:12px}
.body-text{font-size:15px;line-height:25px;color:var(--muted)}
.about .body-text{margin-top:20px;color:#3d3d48}
.about .btn{margin-top:30px}

/* why choose */
.why{top:1320px;height:640px;background:var(--blush)}
.why .copy{position:absolute;left:120px;top:176px;width:360px}
.why .eyebrow{color:var(--ink);font-size:22px;letter-spacing:1px;font-weight:600}
.why .section-title{color:var(--orange);font-size:26px}
.why .rule{margin-top:12px}
.why .body-text{margin-top:18px;font-size:14px;line-height:22px}
.why .btn{margin-top:26px}
.feature{position:absolute;width:260px;height:240px;background:var(--paper);padding:30px 24px;box-shadow:0 8px 22px rgba(0,0,0,.08);border-bottom:4px solid var(--orange)}
.feature h3{font-size:18px;font-weight:700;margin-top:16px}
.feature p{font-size:13px;line-height:20px;color:var(--muted);margin-top:10px}
.feature.is-primary{background:linear-gradient(160deg,var(--orange-light),var(--orange-dark));color:#fff;border-bottom-color:var(--orange-dark)}
.feature.is-primary p{color:#fbe9d6}
.feature .icon{width:46px;height:46px}

/* services */
.services{top:1960px;height:660px}
.services h2{position:absolute;top:56px;width:100%;text-align:center;font-size:30px;font-weight:700}
.service{position:absolute;top:140px;width:308px;height:430px;background:var(--paper);box-shadow:0 10px 24px rgba(0,0,0,.1)}
.service .thumb{height:180px}
.service .card-body{padding:30px 34px}
.service h3{font-size:24px;font-weight:500}
.service p{font-size:13px;line-height:20px;color:var(--muted);margin-top:14px}
.service .btn{margin-top:22px;padding:9px 22px;font-size:11px}
.service.is-featured .card-body{background:linear-gradient(170deg,var(--orange-light),var(--orange-dark));height:250px;color:#fff}
.service.is-featured p{color:#fbe9d6}
.service.is-featured .btn{background:transparent;border:2px solid #fff;color:#fff}

/* testimonials */
.testimonials{top:2620px;height:520px;background:var(--blush)}
.testimonials h2{position:absolute;top:62px;width:100%;text-align:center;font-size:30px;font-weight:700}
.review{position:absolute;top:180px;width:260px;height:220px;background:var(--paper);padding:24px 22px;box-shadow:0 8px 20px rgba(0,0,0,.08)}
.review h4{font-size:14px;line-height:19px;font-weight:700}
.review p{font-size:12px;line-height:17px;color:var(--muted);margin-top:10px}
.reviewer{display:flex;align-items:center;gap:10px;margin-top:14px}
.reviewer .avatar{width:30px;height:30px;border-radius:50%;background:#b9a99c}
.reviewer .name{font-size:10px;font-weight:700;color:var(--ink)}
.stars{color:var(--orange);font-size:12px;letter-spacing:1px}
.dots{position:absolute;top:432px;left:790px;display:flex;gap:8px}
.dots span{width:12px;height:12px;border-radius:50%;background:#c9b9ae}
.dots span.on{background:var(--ink)}

/* quote */
.quote{top:3140px;height:670px}
.quote h2{position:absolute;left:132px;top:134px;font-size:28px;font-weight:500;letter-spacing:1px}
.quote h2 strong{font-weight:800;color:var(--orange)}
.quote .rule{position:absolute;left:132px;top:180px}
.quote-form{position:absolute;left:132px;top:208px;width:412px}
.field{height:46px;background:var(--blush);border-bottom:1px solid var(--line);margin-bottom:20px;padding:10px 14px;font-size:10px;font-weight:700;letter-spacing:.6px;color:#5a5a66}
.field.is-area{height:110px}
.quote-form .btn{margin-top:14px;background:linear-gradient(90deg,var(--orange-dark),var(--orange-light));padding:13px 30px}
.quote .blob{position:absolute;left:590px;top:90px}

/* footer */
.site-footer{top:3812px;height:300px;background:var(--footer)}
.site-footer .brand{left:120px;top:48px}
.site-footer .legal{position:absolute;left:120px;top:158px;font-size:11px;line-height:18px;color:var(--muted)}
.fcol{position:absolute;top:0;height:300px;border-left:1px solid var(--line);padding:52px 0 0 40px}
.fcol h4{font-size:14px;font-weight:700;letter-spacing:.6px}
.fcol ul{list-style:none;margin-top:16px}
.fcol li{font-size:12px;line-height:22px;color:var(--muted)}
.contact-line{display:flex;gap:12px;align-items:flex-start;font-size:12px;line-height:18px;color:var(--muted);margin-top:18px}
.contact-line svg{flex:none}
.social{display:flex;gap:10px;margin-top:18px}
.social span{width:26px;height:26px;border-radius:50%;background:var(--orange)}
</style>
</head>
<body>

<header class="site-header">
  <div class="brand"><span class="mark"></span>NRB Productions</div>
  <nav class="nav">
    <a class="active" href="#">ABOUT US</a>
    <a href="#">SERVICES</a>
    <a href="#">GHOST WRITING</a>
    <a href="#">DIET AUTHORS</a>
    <a href="#">BLOGS</a>
    <a href="#">CONTACT</a>
    <svg class="search" width="18" height="18" viewBox="0 0 18 18"><circle cx="7.5" cy="7.5" r="5.5" fill="none" stroke="#27283a" stroke-width="2"/><line x1="11.5" y1="11.5" x2="16" y2="16" stroke="#27283a" stroke-width="2"/></svg>
  </nav>
</header>

<section class="hero">
  <div class="photo" role="img" aria-label="Writer's hand holding a pen over an open notebook on a wooden desk"></div>
  <div class="shade"></div>
  <p class="kicker">NRB PRODUCTIONS</p>
  <h1>SELF HELP WELLNESS<br>&amp; DEIT AUTHORS</h1>
  <a class="btn btn-solid" href="#">GET A QUOTE</a>
  <svg class="arrow" style="left:20px" width="24" height="40" viewBox="0 0 24 40"><polyline points="18,4 4,20 18,36" fill="none" stroke="#fff" stroke-width="4"/></svg>
  <svg class="arrow" style="right:20px" width="24" height="40" viewBox="0 0 24 40"><polyline points="6,4 20,20 6,36" fill="none" stroke="#fff" stroke-width="4"/></svg>
</section>

<section class="about">
  <svg class="blob" width="560" height="540" viewBox="0 0 560 540">
    <defs><linearGradient id="aboutPhoto" x1="0" y1="0" x2="1" y2="1"><stop offset="0" stop-color="#d7d3cf"/><stop offset=".5" stop-color="#a8432f"/><stop offset="1" stop-color="#ece7e2"/></linearGradient></defs>
    <path d="M0,20 C120,-10 330,10 470,60 C560,95 560,200 520,300 C480,400 420,470 300,500 C190,525 70,490 0,450 Z" fill="url(#aboutPhoto)" role="img" aria-label="Two colleagues reviewing a manuscript together at a laptop"/>
    <path d="M20,480 C110,530 240,540 340,510 C430,480 500,410 540,320" fill="none" stroke="#c77b2b" stroke-width="10" stroke-linecap="round"/>
  </svg>
  <div class="copy">
    <p class="eyebrow">WHO WE ARE</p>
    <h2 class="section-title">ABOUT NRB PRODUCTIONS</h2>
    <div class="rule"></div>
    <p class="body-text">Lorem Ipsum is simply dummy text of the printing and typesetting industry. Lorem Ipsum has been the industry's standard dummy text ever since the 1500s, when an unknown printer took a galley of type and scrambled it to make a type specimen book. It has survived not only five centuries.</p>
    <a class="btn btn-outline" href="#">LEARN MORE</a>
  </div>
</section>

<section class="why">
  <div class="copy">
    <p class="eyebrow">WHY CHOOSE</p>
    <h2 class="section-title">NRB PRODUCTIONS</h2>
    <div class="rule"></div>
    <p class="body-text">Lorem Ipsum is simply dummy text of the printing and typesetting industry. Lorem Ipsum has been the industry's standard dummy text ever since the 1500s, when an unknown printer book.</p>
    <a class="btn btn-outline" href="#">LEARN MORE</a>
  </div>

  <article class="feature is-primary" style="left:532px;top:80px">
    <svg class="icon" viewBox="0 0 46 46"><path d="M10,36 L32,14 L36,18 L14,40 L8,42 Z" fill="none" stroke="#fff" stroke-width="2.5"/><line x1="28" y1="18" x2="32" y2="22" stroke="#fff" stroke-width="2.5"/></svg>
    <h3>SELF HELP</h3>
    <p>Lorem Ipsum is simply dummy text of the printing and typesetting industry. Lorem Ipsum is simply dummy text.</p>
  </article>
  <article class="feature" style="left:820px;top:180px">
    <svg class="icon" viewBox="0 0 46 46"><rect x="8" y="6" width="26" height="34" rx="2" fill="none" stroke="#c77b2b" stroke-width="2.5"/><line x1="14" y1="16" x2="28" y2="16" stroke="#c77b2b" stroke-width="2.5"/><line x1="14" y1="23" x2="28" y2="23" stroke="#c77b2b" stroke-width="2.5"/><line x1="14" y1="30" x2="24" y2="30" stroke="#c77b2b" stroke-width="2.5"/></svg>
    <h3>DIET AUTHORS</h3>
    <p>Lorem Ipsum is simply dummy text of the printing and typesetting industry. Lorem Ipsum is simply dummy text.</p>
  </article>
  <article class="feature" style="left:532px;top:340px">
    <svg class="icon" viewBox="0 0 46 46"><path d="M23,40 C10,30 6,22 6,15 C6,9 11,6 15,6 C19,6 22,9 23,12 C24,9 27,6 31,6 C35,6 40,9 40,15 C40,22 36,30 23,40 Z" fill="none" stroke="#c77b2b" stroke-width="2.5"/></svg>
    <h3>WELLNESS</h3>
    <p>Lorem Ipsum is simply dummy text of the printing and typesetting industry. Lorem Ipsum is simply dummy text.</p>
  </article>
</section>

<section class="services">
  <h2>WHAT WE OFFER</h2>
  <article class="service" style="left:112px">
    <div class="thumb" role="img" aria-label="Close-up of a typewritten page" style="background:linear-gradient(135deg,#f2f2f2,#7a7a7a 60%,#2b2b2b)"></div>
    <div class="card-body">
      <h3>Ghost writing</h3>
      <p>Lorem Ipsum is simply dummy text of the printing and typesetting industry. Lorem Ipsum has been the industry's standard dummy text ever since the.</p>
      <a class="btn btn-solid" href="#">LEARN MORE</a>
    </div>
  </article>
  <article class="service is-featured" style="left:452px">
    <div class="thumb" role="img" aria-label="Editor marking up pages at a desk" style="background:linear-gradient(135deg,#d8c8b8,#8f6a4f 55%,#3b2a22)"></div>
    <div class="card-body">
      <h3>Book Editing</h3>
      <p>Lorem Ipsum is simply dummy text of the printing and typesetting industry. Lorem Ipsum has been the industry's standard dummy text ever since the.</p>
      <a class="btn" href="#">LEARN MORE</a>
    </div>
  </article>
  <article class="service" style="left:792px">
    <div class="thumb" role="img" aria-label="Desk with laptop, notes and coffee during book planning" style="background:linear-gradient(135deg,#5a4332,#b08a62 50%,#e7d9c8)"></div>
    <div class="card-body">
      <h3>Book development</h3>
      <p>Lorem Ipsum is simply dummy text of the printing and typesetting industry. Lorem Ipsum has been the industry's standard dummy text ever since the.</p>
      <a class="btn btn-solid" href="#">LEARN MORE</a>
    </div>
  </article>
</section>

<section class="testimonials">
  <h2>WHAT PEOPLE SAYS</h2>
  <svg class="abs" style="left:180px;top:110px" width="360" height="360" viewBox="0 0 360 360">
    <defs><linearGradient id="booksArt" x1="0" y1="0" x2="1" y2="1"><stop offset="0" stop-color="#b9a6d6"/><stop offset=".55" stop-color="#e6a58c"/><stop offset="1" stop-color="#f3c27f"/></linearGradient></defs>
    <path d="M60,40 C150,0 300,30 330,130 C355,220 290,300 190,310 C90,320 20,260 20,170 C20,110 30,60 60,40 Z" fill="url(#booksArt)" role="img" aria-label="Stack of hardcover books floating on a soft color blob"/>
    <ellipse cx="130" cy="325" rx="40" ry="22" fill="#e9a98f"/>
  </svg>
  <article class="review" style="left:560px">
    <h4>What Clear Story Guides Experienced After Getting</h4>
    <p>Lorem ipsum dolor sit amet, consectetur adipiscing elit, sed do eiusmod tempor incididunt ut labore et dolore magna.</p>
    <div class="reviewer"><span class="avatar"></span><div><div class="name">NADIA BRENT</div><div class="stars">★★★★★</div></div></div>
  </article>
  <article class="review" style="left:840px">
    <h4>What Clear Story Guides Experienced After Getting</h4>
    <p>Lorem ipsum dolor sit amet, consectetur adipiscing elit, sed do eiusmod tempor incididunt ut labore et dolore magna.</p>
    <div class="reviewer"><span class="avatar"></span><div><div class="name">JANE MORROW</div><div class="stars">★★★★★</div></div></div>
  </article>
  <div class="dots"><span></span><span class="on"></span><span></span></div>
</section>

<section class="quote">
  <h2>GET A <strong>FREE QUOTE</strong></h2>
  <div class="rule"></div>
  <form class="quote-form">
    <div class="field">YOUR NAME *</div>
    <div class="field">E-MAIL *</div>
    <div class="field">PHONE *</div>
    <div class="field is-area">YOUR MESSAGE</div>
    <a class="btn btn-solid" href="#">SUBMIT MESSAGE</a>
  </form>
  <svg class="blob" width="540" height="560" viewBox="0 0 540 560">
    <defs><linearGradient id="roomPhoto" x1="0" y1="0" x2="1" y2="1"><stop offset="0" stop-color="#f4e9e2"/><stop offset=".6" stop-color="#edc9bf"/><stop offset="1" stop-color="#d9a27f"/></linearGradient></defs>
    <path d="M80,60 C190,0 400,10 480,110 C545,190 530,330 470,420 C400,520 240,555 130,500 C40,455 10,350 20,240 C28,160 40,90 80,60 Z" fill="url(#roomPhoto)" role="img" aria-label="Pink armchair beside a small table and lamp in a bright room"/>
    <path d="M60,90 C20,170 10,300 60,390" fill="none" stroke="#c77b2b" stroke-width="10" stroke-linecap="round"/>
  </svg>
</section>

<footer class="site-footer">
  <div class="brand"><span class="mark"></span>NRB Productions</div>
  <p class="legal">Copyright 2024 NRB Productions All Rights Reserved.<br>Privacy Policy | Cookies</p>

  <div class="fcol" style="left:440px;width:300px">
    <h4>CONTACT US</h4>
    <div class="contact-line"><svg width="16" height="20" viewBox="0 0 16 20"><path d="M8,19 C3,12 1,9 1,7 A7,7 0 0 1 15,7 C15,9 13,12 8,19 Z" fill="#c77b2b"/><circle cx="8" cy="7" r="2.5" fill="#fff"/></svg><span>418 Redbud Lane, Austin,<br>TX 78701</span></div>
    <div class="contact-line"><svg width="16" height="16" viewBox="0 0 16 16"><path d="M3,1 L6,1 L7,5 L5,6.5 C6,9 7,10 9.5,11 L11,9 L15,10 L15,13 C15,14 14,15 13,15 C6,15 1,10 1,3 C1,2 2,1 3,1 Z" fill="#c77b2b"/></svg><span>+1 512 555 0142</span></div>
    <div class="contact-line"><svg width="18" height="14" viewBox="0 0 18 14"><rect x="1" y="1" width="16" height="12" fill="none" stroke="#c77b2b" stroke-width="2"/><polyline points="1,1 9,8 17,1" fill="none" stroke="#c77b2b" stroke-width="2"/></svg><span>hello@nadiabrentproductions.example</span></div>
  </div>

  <div class="fcol" style="left:740px;width:180px">
    <h4>COMPANY</h4>
    <ul><li>About us</li><li>Services</li><li>Ghost writing</li><li>Diet authors</li><li>Blogs</li><li>Contact</li></ul>
  </div>

  <div class="fcol" style="left:920px;width:200px">
    <h4>FOLLOW US</h4>
    <div class="social"><span></span><span></span><span></span></div>
  </div>
</footer>

</body>
</html>
```